UI/UX Design for AI Photo-to-Video Web Platform (Figma)

I am looking for a modern, high-converting redesign for my Next.js-based web platform. The service allows users to transform old photos into vibrant memories using AI. The design needs to be clean, intuitive, and "mobile-ready" (responsive).
Key Features to Visualize on the Homepage:
Photo Restoration & Colorization: A clear "before/after" visual showing a black-and-white photo turning into a high-quality color photo.
Photo-to-Video Animation: A visual representation of how both B&W and color photos are transformed into dynamic video clips.
Story Creation: A section showing how these photos and videos are combined into a single "Story Video" with background music.
Scope of Work:
Homepage Redesign: A hero section with the core value proposition and a visual walkthrough of the process.
Service/Internal Pages: Redesigning the functional pages where users upload files and manage their projects.
Responsive Design: While the focus is desktop, the layout must be designed with a "Mobile-First" mindset for easy porting to a mobile app later.
Technical Requirements for the Designer:
Tool: Must be designed in Figma.
Structure: Use Figma Auto Layout and Components for all elements (buttons, inputs, cards).
Design System: Provide a clear style guide (Typography, Color Palette, Spacing).
Assets: All icons should be in SVG format.
Style Preference:
Modern, sleek, and trustworthy.
Since the product is about "memories," the vibe should be emotional yet technologically advanced (AI-driven).

```html
<!DOCTYPE html>
<html lang="en">
<head>
<meta charset="utf-8">
<title>Tintwell.ai – New Project</title>
<link rel="stylesheet" href="https://fonts.googleapis.com/css2?family=Plus+Jakarta+Sans:wght@400;500;600;700&display=swap">
<style>
:root{
  --bg:#0d1220;
  --nav:#131a2b;
  --panel:#121a2b;
  --inner:#0b1019;
  --chip:#1a2233;
  --line:#232c3d;
  --text:#ffffff;
  --muted:#8a93a6;
  --dim:#5d6678;
  --purple:#5b2fd6;
  --purple-soft:#3a2670;
  --yellow:#f4b400;
  --amber-soft:#5a4114;
  --blue:#2f80ed;
  --green:#22c55e;
  --violet:#8b5cf6;
}
*{box-sizing:border-box;margin:0;padding:0}
html,body{width:826px;height:1200px;overflow:hidden;background:var(--bg)}
body{font-family:"Plus Jakarta Sans",sans-serif;color:var(--text)}
.page{position:absolute;left:0;top:0;width:1440px;height:2092px;transform:scale(.5736);transform-origin:0 0;background:var(--bg)}
.abs{position:absolute}
svg{display:block}

.nav{left:0;top:0;width:1440px;height:75px;background:var(--nav)}
.brand{left:40px;top:18px;display:flex;align-items:center;gap:12px;font-size:25px;font-weight:500}
.brand-dot{width:38px;height:38px;border-radius:50%;background:var(--yellow)}
.nav-links{left:283px;top:27px;display:flex;gap:48px;font-size:16px;color:var(--muted)}
.nav-links .active{color:#fff}
.bell{left:1274px;top:26px}
.badge{left:1290px;top:21px;width:21px;height:21px;border-radius:50%;background:var(--blue);font-size:13px;text-align:center;line-height:21px}
.avatar{left:1352px;top:14px;width:48px;height:48px;border-radius:50%;background:#222b3c;display:flex;align-items:center;justify-content:center}

.title{font-size:32px;font-weight:600}
.project-input{left:40px;top:214px;width:555px;height:56px;border:1px solid var(--line);background:var(--panel);border-radius:6px;padding:0 23px;line-height:56px;color:var(--muted);font-size:16px}

.plan{left:845px;top:154px;width:555px;height:136px;background:var(--panel);border-radius:16px}
.plan .lbl{font-size:20px;top:24px}
.pill{height:38px;border-radius:19px;padding:0 14px;line-height:38px;font-size:19px}
.storage-bar{left:341px;top:97px;width:182px;height:13px;border-radius:7px;background:#252d3e}
.storage-fill{width:27px;height:13px;border-radius:7px;background:var(--purple)}

.main{left:40px;top:314px;width:1360px;height:704px;background:var(--panel);border:1px solid var(--line);border-radius:16px}
.divider{left:1026px;top:0;width:1px;height:702px;background:var(--line)}
.h2{font-size:29px;font-weight:600}
.sub{font-size:16px;color:var(--muted)}
.drop{left:31px;top:118px;width:971px;height:553px;background:var(--inner);border-radius:14px}
.thumb{border-radius:12px;background:linear-gradient(135deg,#8a8a8a,#3c3c3c 60%,#6d6d6d)}
.remove{left:162px;top:-10px;width:20px;height:20px;border-radius:50%;background:var(--inner);display:flex;align-items:center;justify-content:center}
.addbox{left:196px;top:32px;width:140px;height:140px;border:1px solid #cfd3da;border-radius:12px;display:flex;align-items:center;justify-content:center}
.hint{left:32px;top:196px;font-size:11px;color:var(--dim)}
.prompt{left:32px;top:370px;font-size:19px;color:var(--muted)}
.modes{left:12px;top:433px;width:416px;height:88px;border-radius:44px;background:var(--panel);display:flex;align-items:center;gap:8px;padding:0 20px}
.mode{height:48px;border-radius:24px;background:var(--inner);display:flex;align-items:center;gap:10px;padding:0 18px;font-size:17px;font-weight:500}
.mode.on{background:#fff;color:#111}

.settings{left:1048px;top:0;width:297px}
.lab{font-size:16px;font-weight:500}
.slider-box{left:0;top:190px;width:297px;height:97px;background:var(--inner);border-radius:14px}
.toggle{height:48px;border-radius:24px;line-height:48px;text-align:center;font-size:16px;font-weight:500}
.dur-box{left:0;top:453px;width:297px;height:82px;background:var(--inner);border-radius:14px}
.dur{top:20px;width:62px;height:40px;border-radius:20px;line-height:40px;text-align:center;font-size:16px;background:var(--chip)}
.generate{left:0;top:583px;width:297px;height:56px;border-radius:28px;background:var(--purple);display:flex;align-items:center;justify-content:center;gap:12px;font-size:17px;font-weight:500}

.proc{left:40px;top:1072px;width:1360px;height:474px;background:var(--panel);border-radius:16px}
.row-thumb{width:100px;height:100px;border-radius:8px;background:linear-gradient(135deg,#9a9a9a,#3a3a3a 60%,#777)}
.row-name{font-size:18px}
.row-status{font-size:16px;color:#cfd3da}
.track{width:1102px;height:6px;border-radius:3px;background:#0c111c}
.fill{height:6px;border-radius:3px;background:var(--blue)}
.pct{font-size:16px}

.card{top:1657px;width:440px;height:383px;background:var(--panel);border:1px solid var(--line);border-radius:16px}
.card-img{left:20px;top:20px;width:400px;height:204px}
.card-title{left:20px;top:243px;font-size:25px;font-weight:500}
.card-date{right:24px;top:250px;font-size:16px;color:var(--muted)}
.done{left:20px;top:316px;height:38px;border-radius:19px;background:#0f1524;display:flex;align-items:center;gap:8px;padding:0 14px;font-size:15px;color:var(--blue);font-weight:500}
.done i{width:10px;height:10px;border-radius:50%;background:var(--blue)}
.act{top:312px;width:46px;height:46px;border-radius:6px;display:flex;align-items:center;justify-content:center}
</style>
</head>
<body>
<div class="page">

  <header class="abs nav">
    <div class="abs brand"><span class="brand-dot"></span>Tintwell.ai</div>
    <nav class="abs nav-links"><span class="active">Home</span><span>How its work</span><span>Settings</span><span>Help &amp; Support</span></nav>
    <svg class="abs bell" width="24" height="26" viewBox="0 0 24 26" fill="none" stroke="#fff" stroke-width="2"><path d="M5 18V11a7 7 0 0 1 14 0v7l2 2H3z"/><path d="M9 23h6"/></svg>
    <div class="abs badge">0</div>
    <div class="abs avatar"><svg width="18" height="18" viewBox="0 0 18 18" fill="#0d1220"><circle cx="9" cy="5" r="4"/><path d="M1 17c0-4 4-6 8-6s8 2 8 6z"/></svg></div>
  </header>

  <h1 class="abs title" style="left:40px;top:150px">New Project</h1>
  <div class="abs project-input">Untitled Project...</div>

  <section class="abs plan">
    <div class="abs lbl" style="left:20px">Your Plan</div>
    <div class="abs lbl" style="left:194px">Credits</div>
    <div class="abs lbl" style="left:345px">Storage:</div>
    <div class="abs pill" style="left:20px;top:73px;background:var(--purple-soft);color:#b9a6f5">Professional</div>
    <div class="abs pill" style="left:190px;top:73px;background:var(--amber-soft);color:var(--yellow)">4,740</div>
    <div class="abs" style="left:341px;top:66px;font-size:16px;font-weight:500">200MB/1GB</div>
    <div class="abs storage-bar"><div class="storage-fill"></div></div>
  </section>

  <section class="abs main">
    <h2 class="abs h2" style="left:31px;top:34px">Choose Images</h2>
    <p class="abs sub" style="left:31px;top:80px">Upload photos to generate vintage and real color versions</p>

    <div class="abs drop">
      <div class="abs thumb" role="img" aria-label="Black and white family portrait upload" style="left:32px;top:32px;width:140px;height:140px"></div>
      <div class="abs remove" style="left:162px;top:22px"><svg width="10" height="10" viewBox="0 0 10 10" stroke="#fff" stroke-width="1.6"><path d="M1 1l8 8M9 1l-8 8"/></svg></div>
      <div class="abs addbox"><svg width="16" height="16" viewBox="0 0 16 16" stroke="#fff" stroke-width="1.4"><path d="M8 1v14M1 8h14"/></svg></div>
      <div class="abs hint">Maximum 20 images . 100 MB total . JPG,PNG,GIF,TIFF up to 10MB each</div>
      <div class="abs prompt"><span style="color:#fff">|</span> Type here Prompt to edit images</div>
      <div class="abs modes">
        <div class="mode on"><svg width="20" height="20" viewBox="0 0 20 20" fill="none" stroke="#111" stroke-width="1.8"><rect x="2" y="2" width="16" height="16" rx="2"/><path d="M2 15l5-5 4 4 3-3 4 4"/></svg>Image</div>
        <div class="mode"><svg width="20" height="20" viewBox="0 0 20 20" fill="none" stroke="#fff" stroke-width="1.8"><circle cx="10" cy="10" r="8"/><rect x="7" y="7" width="6" height="6" fill="#fff"/></svg>Video</div>
        <div class="mode"><svg width="22" height="20" viewBox="0 0 22 20" fill="none" stroke="#fff" stroke-width="1.8"><rect x="2" y="7" width="16" height="11" rx="1"/><path d="M2 7l15-4 1 3M7 6l-2-3M12 5l-2-3"/></svg>Studio</div>
      </div>
    </div>

    <div class="abs divider"></div>

    <div class="abs settings">
      <h2 class="abs h2" style="left:0;top:34px;white-space:nowrap">Image Settings</h2>
      <p class="abs" style="left:0;top:80px;font-size:14px;color:var(--muted);white-space:nowrap">Customize by your preferances</p>
      <div class="abs" style="left:0;top:115px;width:297px;height:1px;background:var(--line)"></div>
      <div class="abs lab" style="left:0;top:157px">Color</div>
      <div class="abs slider-box">
        <div class="abs" style="left:20px;top:19px;font-size:14px">Normal</div>
        <div class="abs" style="left:125px;top:19px;font-size:14px">Vintage</div>
        <div class="abs" style="right:18px;top:19px;font-size:14px">Real</div>
        <div class="abs" style="left:20px;top:56px;width:260px;height:12px;border-radius:6px;background:#273042"></div>
        <div class="abs" style="left:19px;top:46px;width:14px;height:32px;border-radius:7px;background:var(--yellow)"></div>
      </div>
      <div class="abs lab" style="left:0;top:309px;white-space:nowrap">Focus Detact</div>
      <div class="abs toggle" style="left:-2px;top:344px;width:100px;background:var(--yellow);color:#111">Auto</div>
      <div class="abs toggle" style="left:118px;top:344px;width:100px;background:var(--inner)">Manual</div>
      <div class="abs lab" style="left:0;top:419px">Duration</div>
      <div class="abs dur-box">
        <div class="abs dur" style="left:19px">6s</div>
        <div class="abs dur" style="left:118px;background:var(--yellow);color:#111">10s</div>
        <div class="abs dur" style="left:217px">30s</div>
      </div>
      <div class="abs generate"><svg width="22" height="22" viewBox="0 0 22 22" fill="none" stroke="#fff" stroke-width="1.8"><path d="M3 19L14 8M15 2v4M13 4h4M19 9v3M17.5 10.5h3M7 3v3M5.5 4.5h3"/></svg>Generate</div>
      <div class="abs" style="left:0;top:655px;width:297px;text-align:center;font-size:12px;color:#cfd3da">20 Credits wil be used</div>
    </div>
  </section>

  <section class="abs proc">
    <h3 class="abs" style="left:28px;top:34px;font-size:20px;font-weight:600">Processing (3)</h3>
    <div class="abs" style="right:37px;top:34px;font-size:20px;color:var(--yellow);font-weight:500">See All</div>

    <div class="abs row-thumb" role="img" aria-label="Family portrait in progress" style="left:28px;top:94px"></div>
    <div class="abs row-name" style="left:143px;top:99px">Family Photo 1962</div>
    <div class="abs row-status" style="left:143px;top:135px">Processing...</div>
    <div class="abs track" style="left:143px;top:161px"><div class="fill" style="width:757px"></div></div>
    <div class="abs pct" style="left:1281px;top:156px">60%</div>

    <div class="abs row-thumb" role="img" aria-label="Old portrait of father and child in progress" style="left:28px;top:220px"></div>
    <div class="abs row-name" style="left:143px;top:219px">Old Memories</div>
    <div class="abs row-status" style="left:143px;top:255px">Processing...</div>
    <div class="abs track" style="left:143px;top:295px"><div class="fill" style="width:357px"></div></div>
    <div class="abs pct" style="left:1281px;top:291px">30%</div>

    <div class="abs row-thumb" role="img" aria-label="Family portrait in progress" style="left:28px;top:346px"></div>
    <div class="abs row-name" style="left:143px;top:351px">Family Photo 1962</div>
    <div class="abs row-status" style="left:143px;top:387px">Processing...</div>
    <div class="abs track" style="left:143px;top:413px"><div class="fill" style="width:757px"></div></div>
    <div class="abs pct" style="left:1281px;top:408px">60%</div>
  </section>

  <h2 class="abs title" style="left:40px;top:1582px">Recently Created</h2>
  <div class="abs" style="right:40px;top:1590px;font-size:20px;color:var(--purple);font-weight:500;color:#6a3ff0">See All</div>

  <article class="abs card" style="left:40px">
    <div class="abs card-img" role="img" aria-label="Colorized family portrait" style="background:linear-gradient(135deg,#6f7a3c,#1d2a4a 45%,#3a4f86 70%,#9aa36a)"></div>
    <div class="abs card-title">Family Photo 1960</div>
    <div class="abs card-date">April 12 2026</div>
    <div class="abs done"><i></i>Done</div>
    <div class="abs act" style="left:210px;background:var(--green)"><svg width="18" height="18" viewBox="0 0 18 18" fill="none" stroke="#fff" stroke-width="1.8"><path d="M9 2v10M5 8l4 4 4-4M2 15h14"/></svg></div>
    <div class="abs act" style="left:286px;background:var(--violet)"><svg width="18" height="18" viewBox="0 0 18 18" fill="none" stroke="#fff" stroke-width="1.6"><circle cx="13" cy="4" r="2"/><circle cx="4" cy="9" r="2"/><circle cx="13" cy="14" r="2"/><path d="M6 8l5-3M6 10l5 3"/></svg></div>
    <div class="abs act" style="left:364px;background:var(--yellow)"><svg width="18" height="18" viewBox="0 0 18 18" fill="none" stroke="#fff" stroke-width="1.8"><path d="M15 3L7 11M7 11l-3 1-1 3 3-1z"/></svg></div>
  </article>

  <article class="abs card" style="left:500px">
    <div class="abs card-img" role="img" aria-label="Colorized portrait of father holding a child" style="background:linear-gradient(135deg,#d8cfb7,#6b6a68 45%,#2b3552 70%,#a8825a)"></div>
    <div class="abs card-title">Family Photo 1960</div>
    <div class="abs card-date">April 12 2026</div>
    <div class="abs done"><i></i>Done</div>
    <div class="abs act" style="left:210px;background:var(--green)"><svg width="18" height="18" viewBox="0 0 18 18" fill="none" stroke="#fff" stroke-width="1.8"><path d="M9 2v10M5 8l4 4 4-4M2 15h14"/></svg></div>
    <div class="abs act" style="left:286px;background:var(--violet)"><svg width="18" height="18" viewBox="0 0 18 18" fill="none" stroke="#fff" stroke-width="1.6"><circle cx="13" cy="4" r="2"/><circle cx="4" cy="9" r="2"/><circle cx="13" cy="14" r="2"/><path d="M6 8l5-3M6 10l5 3"/></svg></div>
    <div class="abs act" style="left:364px;background:var(--yellow)"><svg width="18" height="18" viewBox="0 0 18 18" fill="none" stroke="#fff" stroke-width="1.8"><path d="M15 3L7 11M7 11l-3 1-1 3 3-1z"/></svg></div>
  </article>

  <article class="abs card" style="left:960px">
    <div class="abs card-img" role="img" aria-label="Colorized portrait of a man in a suit outdoors" style="background:linear-gradient(135deg,#5d7a2e,#2e4a22 40%,#23335e 65%,#1a1f2c)"></div>
    <div class="abs card-title">Family Photo 1960</div>
    <div class="abs card-date">April 12 2026</div>
    <div class="abs done"><i></i>Done</div>
    <div class="abs act" style="left:210px;background:var(--green)"><svg width="18" height="18" viewBox="0 0 18 18" fill="none" stroke="#fff" stroke-width="1.8"><path d="M9 2v10M5 8l4 4 4-4M2 15h14"/></svg></div>
    <div class="abs act" style="left:286px;background:var(--violet)"><svg width="18" height="18" viewBox="0 0 18 18" fill="none" stroke="#fff" stroke-width="1.6"><circle cx="13" cy="4" r="2"/><circle cx="4" cy="9" r="2"/><circle cx="13" cy="14" r="2"/><path d="M6 8l5-3M6 10l5 3"/></svg></div>
    <div class="abs act" style="left:364px;background:var(--yellow)"><svg width="18" height="18" viewBox="0 0 18 18" fill="none" stroke="#fff" stroke-width="1.8"><path d="M15 3L7 11M7 11l-3 1-1 3 3-1z"/></svg></div>
  </article>

</div>
</body>
</html>
```